Einladungskarten-Design für Schützenverein
super gute Zusammenarbeit. Werde für weitere Arbeiten gerne darauf zurückkommen.
Zielgruppe
Wir sind ein Schützenverein und möchten mit einem neuzeitlichen Design für unser traditionelles Grümpelschiessen Werbung machen und die jüngere Generation für diesen schönen Sport begeistern.

```html
<!DOCTYPE html>
<html lang="de">
<head>
<meta charset="utf-8">
<title>Einladung zum Grümpelschiessen 2021</title>
<link href="https://fonts.googleapis.com/css2?family=Montserrat:wght@800&family=Lato:wght@700;900&display=swap" rel="stylesheet">
<style>
  :root {
    --yellow: #e6c200;
    --blue: #1f2a78;
    --white: #ffffff;
    --grass-dark: #4c8a28;
    --grass-light: #c8c21c;
    --backdrop: #e8e8e8;
  }
  * { box-sizing: border-box; margin: 0; padding: 0; }
  html, body { width: 1200px; height: 800px; overflow: hidden; }
  body { background: var(--backdrop); font-family: "Lato", sans-serif; }

  .flyer {
    position: absolute; left: 330px; top: 18px;
    width: 540px; height: 764px; overflow: hidden;
    background: linear-gradient(180deg, var(--grass-dark) 35%, #6ea12a 65%, var(--grass-light) 100%);
    box-shadow: 0 10px 30px rgba(0,0,0,.25);
  }
  .hero-photo {
    position: absolute; left: 0; top: 0; width: 540px; height: 300px;
    background: linear-gradient(160deg, #7a8a3a 0%, #a9b448 40%, #c7c23a 70%, #6c9a2c 100%);
  }
  .hero-photo::after {
    content: ""; position: absolute; left: 0; right: 0; bottom: 0; height: 80px;
    background: linear-gradient(180deg, transparent, var(--grass-dark));
  }

  .club-mark {
    position: absolute; right: 30px; top: 34px; width: 112px; height: 112px;
    background: var(--white); padding: 10px;
    display: flex; flex-direction: column; justify-content: space-between;
  }
  .club-mark .club-name {
    font-family: "Lato", sans-serif; font-weight: 900; font-size: 13px;
    line-height: 1.2; color: var(--blue); text-transform: uppercase;
  }
  .club-mark .club-square { width: 26px; height: 26px; background: var(--yellow); }

  .headline { font-family: "Montserrat", sans-serif; font-weight: 800; color: var(--white); }
  .headline span { position: absolute; display: block; line-height: 1; white-space: nowrap; }
  .headline .line-invite { left: 90px; top: 250px; background: var(--yellow); font-size: 34px; padding: 6px 12px 4px; }
  .headline .line-event  { left: 30px; top: 294px; background: var(--blue); font-size: 36px; padding: 7px 14px 5px; }
  .headline .line-year   { left: 190px; top: 344px; background: var(--yellow); font-size: 62px; padding: 6px 14px 4px; }

  .details { position: absolute; top: 436px; left: 0; width: 540px; color: var(--white); }
  .when {
    position: absolute; left: 30px; width: 200px; text-align: right;
    font-size: 19px; line-height: 1.15;
  }
  .when .day { font-size: 34px; font-weight: 900; }
  .divider { position: absolute; left: 244px; top: 4px; width: 3px; height: 196px; background: var(--white); }
  .facts { position: absolute; left: 258px; width: 266px; font-size: 14px; line-height: 1.2; }
  .facts dt { color: var(--yellow); }
  .facts dd { margin-bottom: 2px; }
  .facts .venue { color: var(--yellow); text-transform: uppercase; }

  .shooters-art {
    position: absolute; left: 20px; top: 580px; width: 210px; height: 70px;
    background: linear-gradient(90deg, rgba(31,42,120,.85), rgba(31,42,120,.3));
  }

  .footer-band { position: absolute; left: 0; top: 650px; width: 540px; height: 114px; }
  .footer-band svg { position: absolute; inset: 0; }
  .footer-band .welcome {
    position: absolute; left: 24px; right: 24px; top: 12px;
    color: var(--white); font-size: 17px; font-weight: 900; text-align: center; line-height: 1.25;
  }
  .footer-band .web {
    position: absolute; right: 28px; bottom: 8px;
    color: var(--blue); font-weight: 900; font-size: 18px;
  }
</style>
</head>
<body>
  <main class="flyer">
    <div class="hero-photo" role="img" aria-label="Foto: junge Schützin liegend mit Gewehr im Wald"></div>

    <div class="club-mark">
      <span class="club-name">Schützenverein Talhofen</span>
      <span class="club-square"></span>
    </div>

    <h1 class="headline">
      <span class="line-invite">EINLADUNG ZUM</span>
      <span class="line-event">GRÜMPELSCHIESSEN</span>
      <span class="line-year">2021</span>
    </h1>

    <section class="details">
      <p class="when">
        <span class="day">Sonntag</span><br>
        29. August<br>
        08.00 - 12.00<br>
        Uhr durchgehend
      </p>
      <div class="divider"></div>
      <dl class="facts">
        <dt>Wo :</dt>
        <dd><span class="venue">Beim Schützenhaus Talhofen</span><br>(Parkplätze bei der Talstation der Sonnalpbahn)</dd>
        <dt>Wer :</dt>
        <dd>Einzel, Paare und Familien &gt; einfach jedermann ob jung ob alt aus nah und fern, Frau und Mann</dd>
        <dt>Unser Angebot :</dt>
        <dd>Grümpelstich und Festwirtschaft mit Mittags -menü in herrlicher Umgebung</dd>
      </dl>
    </section>

    <div class="shooters-art" role="img" aria-label="Illustration: Silhouetten liegender Schützen"></div>

    <footer class="footer-band">
      <svg width="540" height="114" viewBox="0 0 540 114" aria-hidden="true">
        <rect x="0" y="0" width="540" height="114" fill="var(--yellow)"/>
        <polygon points="0,0 540,0 540,72 300,72 282,84 0,84" fill="var(--blue)"/>
      </svg>
      <p class="welcome">Wir laden Sie herzlich zu einem gemütlichen Sonntag ein und freuen uns auf Ihren Besuch und Ihre Teilnahme.</p>
      <p class="web">www.svtalhofen.ch</p>
    </footer>
  </main>
</body>
</html>
```